Brochure for Veterinary Acupuncture and Physical Therapy
Willow Creek Pet Clinic
Putting the heart into healing
I am a veterinarian. My business is to travel from between existing veterinary practices to do acupucture and physical therapy with dogs and cats. This brochure will be something for the veterinary clinic to give their client about this service.
Animals
Veterinary pet owners
3 fold brochure
Photos and logo. Text will be coming in a separate upload. I'm not sure how much text is appropriate, so for now, can you put empty text boxes in designs so I can see how it might lay out? One section should be about me (picture of me with the dog), one section about acupuncture and one about physical therapy. Then another text box about how to schedule an appointment.
Me
Physical therapy picture
website: willowcreekpetclinic.net
email: willowcreekvet@postbloom.net
Also needs a facebook symbol
My business card, if that helps
Conditions treated -- depending on space I can shorten the physical therapy information
Overview
This is about me
Scheduling
New "training"
New mission

```html
<!DOCTYPE html>
<html lang="en">
<head>
<meta charset="utf-8">
<title>Willow Creek Pet Clinic – Trifold Brochure</title>
<link href="https://fonts.googleapis.com/css2?family=Open+Sans:ital,wght@0,400;0,600;0,700;1,600&family=Lato:wght@700;900&display=swap" rel="stylesheet">
<style>
  :root{
    --bg:#e9e4dc;
    --paper:#ffffff;
    --navy:#1d2f7a;
    --blue:#2c47b8;
    --blue-light:#4a63cf;
    --green:#2f9a3e;
    --green-light:#7cc243;
    --ink:#2b2b2b;
    --muted:#5a5a5a;
  }
  *{box-sizing:border-box;margin:0;padding:0}
  html,body{width:1200px;height:562px;overflow:hidden;background:var(--bg);font-family:"Open Sans",Arial,sans-serif;color:var(--ink)}
  .spread{position:absolute;display:flex;box-shadow:0 3px 10px rgba(0,0,0,.25)}
  .spread--outside{left:36px;top:92px;width:559px;height:405px}
  .spread--inside{left:612px;top:66px;width:568px;height:446px}
  .panel{position:relative;height:100%;overflow:hidden}
  .photo{position:absolute}
  .brand{display:flex;align-items:center;gap:6px;font-family:"Lato",Arial,sans-serif;font-weight:900;text-transform:uppercase;letter-spacing:.3px;line-height:1}
  .brand__dot{width:9px;height:9px;border-radius:50%;background:var(--green-light);flex:none}
  .small{font-size:5.2px;line-height:1.45}
  h3{font-family:"Lato",Arial,sans-serif;font-weight:700}

  /* outside: about */
  .about{width:162px;background:var(--paper)}
  .about .photo{left:0;top:0;width:162px;height:180px;background:linear-gradient(160deg,#8a6b55,#c9b8a6 55%,#6b6f8a)}
  .about__body{position:absolute;left:10px;top:192px;right:10px}
  .about h3{font-size:6.5px;color:var(--navy);margin-bottom:4px;text-transform:uppercase}
  .about p{color:var(--muted);margin-bottom:4px}

  /* outside: scheduling */
  .schedule{width:202px;background:linear-gradient(180deg,var(--blue) 0%,var(--navy) 100%);color:#fff}
  .schedule .photo{left:69px;top:22px;width:64px;height:64px;border-radius:50%;border:3px solid #fff;background:radial-gradient(circle,#d8c3a5,#8b6a4a)}
  .schedule .brand{position:absolute;left:40px;top:112px;font-size:9px;color:#fff}
  .schedule__body{position:absolute;left:16px;top:150px;right:16px}
  .schedule h3{font-size:7px;margin-bottom:5px}
  .schedule p{margin-bottom:8px;color:#dfe5ff}
  .schedule .contact{position:absolute;left:16px;bottom:40px;right:16px}
  .contact-row{display:flex;align-items:center;gap:4px;font-size:5.4px;margin-top:4px}
  .contact-row svg{width:7px;height:7px;flex:none}

  /* outside: cover */
  .cover{width:195px;background:var(--paper)}
  .cover .brand{position:absolute;left:18px;top:16px;font-size:11px;color:var(--blue)}
  .cover__frame{position:absolute;left:0;top:58px;width:195px;height:347px;background:var(--navy)}
  .cover .photo{left:18px;top:76px;width:160px;height:200px;background:linear-gradient(170deg,#5a7ab0,#d9b07a 45%,#3b2a20)}
  .cover__curve{position:absolute;left:0;top:270px;width:195px;height:50px}
  .cover__url{position:absolute;left:0;right:0;top:352px;text-align:center;font-size:8px;font-weight:600;color:#fff}

  /* inside */
  .inside-a{width:190px;background:var(--paper)}
  .inside-a__body{position:absolute;left:10px;top:12px;right:10px}
  .inside-a__body p{color:var(--muted);margin-bottom:5px}
  .inside-a .photo{left:10px;top:258px;width:150px;height:150px;background:linear-gradient(160deg,#c6d8c0,#6b4a30 55%,#2b1f18)}
  .inside-a__stripe{position:absolute;left:165px;top:258px;width:6px;height:150px;background:var(--green)}
  .inside-b{width:190px;background:var(--paper)}
  .inside-b .photo{left:0;top:0;width:190px;height:130px;background:linear-gradient(180deg,#6aa6dc,#e6eef5 60%,#7aa55a)}
  .inside-b__head{position:absolute;left:0;top:136px;width:190px;height:30px;background:var(--green);color:#fff;display:flex;align-items:center;padding:0 12px;font-size:7.5px}
  .condition-list{position:absolute;left:16px;top:176px;right:12px;list-style:none;font-size:5.6px;color:var(--ink)}
  .condition-list li{display:flex;align-items:center;gap:4px;margin-bottom:2.6px}
  .condition-list li::before{content:"";width:3px;height:3px;border-radius:50%;background:var(--green);flex:none}
  .inside-c{width:188px;background:var(--paper)}
  .inside-c__head{height:36px;background:var(--blue);color:#fff;display:flex;align-items:center;padding:0 10px;font-size:7.5px;line-height:1.25}
  .therapy-list{list-style:none;padding:8px 10px 0}
  .therapy-list li{font-size:5.2px;line-height:1.4;color:var(--muted);margin-bottom:5px}
  .therapy-list b{color:var(--navy)}
  .tagline-band{position:absolute;left:0;bottom:0;width:568px;height:38px;background:linear-gradient(90deg,var(--green),var(--green-light));color:#fff;display:flex;align-items:center;justify-content:center;font-style:italic;font-weight:600;font-size:11px;letter-spacing:.6px}
</style>
</head>
<body>

<section class="spread spread--outside">
  <article class="panel about">
    <div class="photo" role="img" aria-label="Photo of the veterinarian hugging a shaggy dog"></div>
    <div class="about__body">
      <h3>About Dr. Maren Holt</h3>
      <p class="small">Dr. Holt graduated from veterinary school and has worked with companion animals for many years. She later trained in veterinary acupuncture and canine rehabilitation to help pets recover comfort and mobility.</p>
      <p class="small">She now travels between partner clinics, bringing gentle, integrative care to dogs and cats close to home. Her goal is simple: to put the heart into every treatment and support each family through recovery.</p>
    </div>
  </article>

  <article class="panel schedule">
    <div class="photo" role="img" aria-label="Round photo of a small dog"></div>
    <div class="brand"><span class="brand__dot"></span>Willow Creek<br>Pet Clinic</div>
    <div class="schedule__body">
      <h3>Scheduling an appointment</h3>
      <p class="small">Ask your regular veterinarian about a referral for acupuncture or physical therapy. Sessions are held at your clinic on scheduled visit days.</p>
      <h3>Please contact your veterinarian for more information.</h3>
    </div>
    <div class="contact">
      <div class="contact-row"><svg viewBox="0 0 10 10"><rect x="1" y="2" width="8" height="6" fill="none" stroke="#fff"/><path d="M1 2l4 3 4-3" fill="none" stroke="#fff"/></svg>willowcreekvet@postbloom.net</div>
      <div class="contact-row"><svg viewBox="0 0 10 10"><path d="M2 1h2l1 2-1 1c1 1 1 2 2 2l1-1 2 1v2c-4 0-7-3-7-7z" fill="#fff"/></svg>(555) 014-2290</div>
      <div class="contact-row"><svg viewBox="0 0 10 10"><rect x="1" y="1" width="8" height="8" rx="1" fill="#fff"/></svg>Follow us online</div>
    </div>
  </article>

  <article class="panel cover">
    <div class="brand"><span class="brand__dot"></span>Willow Creek Pet Clinic</div>
    <div class="cover__frame"></div>
    <div class="photo" role="img" aria-label="Photo of a tan dog receiving acupuncture"></div>
    <svg class="cover__curve" viewBox="0 0 195 50" preserveAspectRatio="none"><path d="M0 30 Q100 0 195 22 L195 50 L0 50Z" fill="var(--green)"/><path d="M0 38 Q100 10 195 30 L195 50 L0 50Z" fill="var(--navy)"/></svg>
    <div class="cover__url">willowcreekpetclinic.net</div>
  </article>
</section>

<section class="spread spread--inside">
  <article class="panel inside-a">
    <div class="inside-a__body">
      <p class="small"><b>Acupuncture</b> is the placement of fine needles at specific points on the body to relieve pain, reduce inflammation and support natural healing. It has been used for centuries and is safe, gentle and well tolerated by most pets.</p>
      <p class="small">Many animals relax during treatment, and some even fall asleep. Sessions usually last twenty to thirty minutes and a short course of visits is often recommended.</p>
      <p class="small">Acupuncture works well alongside conventional medicine and can help reduce the need for some medications in older or sensitive pets.</p>
      <p class="small">Your veterinarian will help decide whether it is right for your pet.</p>
    </div>
    <div class="photo" role="img" aria-label="Photo of a young black and tan dog"></div>
    <div class="inside-a__stripe"></div>
  </article>

  <article class="panel inside-b">
    <div class="photo" role="img" aria-label="Photo of a dog leaping over an agility jump"></div>
    <h3 class="inside-b__head">Conditions Commonly Treated with Acupuncture</h3>
    <ul class="condition-list">
      <li>Arthritis</li><li>Back and neck pain</li><li>Disc disease</li><li>Hip dysplasia</li>
      <li>Muscle injuries</li><li>Nerve injuries</li><li>Chronic pain</li><li>Digestive disorders</li>
      <li>Skin allergies</li><li>Kidney disease</li><li>Seizures</li><li>Urinary problems</li>
      <li>Post-surgical recovery</li><li>Senior wellness</li>
    </ul>
  </article>

  <article class="panel inside-c">
    <h3 class="inside-c__head">Veterinary physical therapy and rehabilitation</h3>
    <ul class="therapy-list">
      <li><b>Underwater treadmill</b> – builds strength while water supports the joints.</li>
      <li><b>Therapeutic exercise</b> – guided movement to restore balance and range.</li>
      <li><b>Laser therapy</b> – light energy to ease pain and speed tissue repair.</li>
      <li><b>Massage</b> – relaxes tight muscles and improves circulation.</li>
      <li><b>Electrical stimulation</b> – mild current to reduce pain and build muscle.</li>
      <li><b>Heat and cold</b> – simple care to calm swelling and soreness.</li>
      <li><b>Home programs</b> – easy exercises to continue progress at home.</li>
    </ul>
  </article>

  <div class="tagline-band">Putting the heart in healing</div>
</section>

</body>
</html>
```